Book cover for a feel-good story

Creation of a cover for the book: "A lantern on a window sill"

Title: "A lantern on a windowsill" (The English translation should not appear)
Author: "Margaux Dubrac"
Publisher: "Editions Corvelle" (should be at the bottom of the page)
Format: 14 x 20.5 cm

The story :
A young single woman (32 years old) is a blogger, she has a passion for shoes.
She has pink hair, just because she likes it. She loves flowers

The text is a humorous story of the woman and the relationship with her mother, similar to Harriet Pemble stories.
A feel good text +++

(The words "diamond" and "shoe box" are not keyword, they do not call for representation in the image. They are just a citation from the book)

Enclosed (joined files): examples of styles' cover that would have suited.

Teenagers, young adults

Book

• shoes, pink hair, flowers
• Diamond, box of shoes

```html
<!DOCTYPE html>
<html lang="fr">
<head>
<meta charset="utf-8">
<title>Une lanterne sur le rebord de la fenêtre — couverture</title>
<link rel="stylesheet" href="https://fonts.googleapis.com/css2?family=Fredoka:wght@500;600;700&family=Open+Sans:wght@400&family=Montserrat:wght@800&family=Josefin+Sans:wght@700&display=swap">
<style>
  :root {
    --saffron: #fdc144;
    --charcoal: #4f4c4a;
    --white: #ffffff;
    --rose: #e02a58;
    --rose-deep: #d92454;
    --cream: #fde8a6;
    --ink: #2b2622;
  }
  * { margin: 0; padding: 0; box-sizing: border-box; }
  html, body { width: 1200px; height: 819px; overflow: hidden; background: var(--saffron); }
  .cover { position: relative; width: 1200px; height: 819px; background: var(--saffron); overflow: hidden; }

  .title { position: absolute; text-align: center; font-family: "Fredoka", sans-serif; line-height: 1; }
  .title .line-top, .title .line-mid { color: var(--charcoal); font-weight: 700; text-transform: uppercase; display: block; white-space: nowrap; }
  .title .line-sub { color: var(--white); font-weight: 600; display: block; white-space: nowrap; }

  .back-cover { position: absolute; left: 0; top: 0; width: 565px; height: 819px; }
  .back-cover .title { left: 0; width: 556px; top: 98px; }
  .back-cover .line-top { font-size: 44px; letter-spacing: -0.5px; }
  .back-cover .line-mid { font-size: 44px; margin-top: 2px; letter-spacing: -0.5px; }
  .back-cover .line-sub { font-size: 36px; margin-top: 2px; }
  .blurb { position: absolute; left: 55px; top: 252px; width: 445px; font-family: "Open Sans", sans-serif; font-size: 12.6px; line-height: 22.8px; color: var(--white); }
  .blurb p { text-align: justify; margin-bottom: 22.8px; }
  .blurb p.lead { text-align: center; }

  .spine { position: absolute; left: 566px; top: 0; width: 70px; height: 819px; display: flex; justify-content: center; }
  .spine-title { writing-mode: vertical-rl; font-family: "Fredoka", sans-serif; font-weight: 600; font-size: 39px; line-height: 1; margin-top: 42px; white-space: nowrap; color: var(--charcoal); }
  .spine-title .accent { color: var(--white); }

  .front-cover { position: absolute; left: 641px; top: 0; width: 559px; height: 819px; }
  .front-cover .title { left: 0; width: 559px; top: 62px; }
  .front-cover .line-top { font-size: 60px; letter-spacing: -0.5px; }
  .front-cover .line-mid { font-size: 60px; margin-top: 2px; letter-spacing: -0.5px; }
  .front-cover .line-sub { font-size: 50px; margin-top: 2px; }
  .portrait { position: absolute; left: 0; top: 290px; width: 559px; height: 529px; }
  .author { position: absolute; left: 0; width: 559px; top: 694px; text-align: center; font-family: "Montserrat", sans-serif; font-weight: 800; font-size: 37px; line-height: 1; color: var(--saffron); letter-spacing: 0.5px; }
  .publisher { position: absolute; left: 0; width: 559px; top: 766px; text-align: center; font-family: "Josefin Sans", sans-serif; font-weight: 700; font-size: 14px; line-height: 1; letter-spacing: 3px; color: var(--ink); }
</style>
</head>
<body>
<main class="cover">
  <section class="back-cover">
    <h2 class="title">
      <span class="line-top">Une lanterne</span>
      <span class="line-mid">sur le rebord</span>
      <span class="line-sub">de la fenêtre</span>
    </h2>
    <div class="blurb">
      <p class="lead">Lou is thirty-two, single and a blogger with a passion for shoes. Her hair is pink, just because she likes it. She loves flowers.</p>
      <p>Between two posts and a new pair of heels, Lou tries to survive her mother, who calls every morning with advice nobody asked for. A funny, tender story about family, love and the small things that matter, written with the warmth of the Harriet Pemble books. Light, sharp and full of heart, it is pure feel-good.</p>
      <p>When a lantern appears on her windowsill one winter night, Lou starts asking questions she has avoided for years. Her mother has answers, of course, but never the right ones. Between laughter, quarrels and long phone calls, the two women slowly learn to look at each other again, and to forgive a little.</p>
      <p>Margaux Dubrac writes with humour and tenderness about the ties that hold us, the dreams we keep in boxes and the courage it takes to open them. A bright, generous novel for anyone who has ever loved their mother, argued with her, and called her straight back the very next morning anyway.</p>
    </div>
  </section>

  <section class="spine">
    <p class="spine-title">Une lanterne sur le rebord <span class="accent">de la fenêtre</span></p>
  </section>

  <section class="front-cover">
    <h1 class="title">
      <span class="line-top">Une lanterne</span>
      <span class="line-mid">sur le rebord</span>
      <span class="line-sub">de la fenêtre</span>
    </h1>
    <svg class="portrait" viewBox="0 0 559 529" preserveAspectRatio="none" role="img" aria-label="Illustration of a young woman in profile with long flowing pink hair and a crown of flowers and leaves">
      <defs>
        <radialGradient id="portrait-tone" cx="300" cy="420" r="300" gradientUnits="userSpaceOnUse">
          <stop offset="0" stop-color="#fde8a6"/>
          <stop offset="0.35" stop-color="#f7c8a0"/>
          <stop offset="0.7" stop-color="#e4456a"/>
          <stop offset="1" stop-color="#d92454"/>
        </radialGradient>
      </defs>
      <path d="M0 529 L0 450 C20 360 30 260 80 170 C130 80 200 20 300 12 C400 6 490 40 559 90 L559 529 Z" fill="url(#portrait-tone)"/>
    </svg>
    <p class="author">MARGAUX DUBRAC</p>
    <p class="publisher">EDITIONS CORVELLE</p>
  </section>
</main>
</body>
</html>
```